Magician | Speaker looks for an innovative business card design

I'm a magician and public speaker offering artistic and modern magical experiences.
I'm based in Brussels (Belgium.) I love magic performed up-close, creating a space of intimacy, even when I'm on stage.
The final design should communicate professionalism, elegance, artistry, and a friendly kind personality

I would like to see designs based either on my photos and/or the way I sign my name Remy Vok (see attached files for more info.)
Additional photos and more info about what I offer can be seen at www.remy-vok.net

My current business card design is also attached. I like the fact that the reverse of my current design includes quotes from master magicians about magic, changing the way my participants see the art of magic.

Note: I would like a double-sided card design. However, I need white space on the reverse to be able to write things on for my performances.

Details to include on the card:
Artist name: Remy Vok
Offer: magician + (public) speaker or magic + (public) speaking (the + sign can be replaced by another character, like a bullet or a pipe)
Phone: +32 471 265 903
Email: book@remy-vok.net
(optional) Website: www.remy-vok.net or remy-vok.net

Target Market(s)

Corporate, organisations, companies as well as individuals

Industry/Entity Type

Artists

Colors

Designer to choose colors to be used in the design.

Requirements
Nice to have
• A side with a mirror could be nice

```html
<!DOCTYPE html>
<html lang="en">
<head>
<meta charset="utf-8">
<title>Remy Vok – Business Card</title>
<link href="https://fonts.googleapis.com/css2?family=Raleway:ital,wght@0,400;0,500;0,700;1,400&display=swap" rel="stylesheet">
<style>
  :root {
    --stage: #e9e6e4;
    --card: #ffffff;
    --red: #f21c2a;
    --red-soft: #f7545e;
    --ink: #e5265a;
    --shadow: rgba(40, 20, 30, 0.18);
  }
  html, body {
    margin: 0;
    width: 1200px;
    height: 800px;
    overflow: hidden;
    background: var(--stage);
    font-family: "Raleway", sans-serif;
  }
  .stage {
    position: relative;
    width: 1200px;
    height: 800px;
  }
  .card {
    position: absolute;
    top: 250px;
    width: 520px;
    height: 300px;
    background: var(--card);
    box-shadow: 0 10px 30px var(--shadow);
    overflow: hidden;
  }
  .card--back { left: 60px; }
  .card--front { left: 620px; }

  .art-area {
    position: absolute;
    background: linear-gradient(135deg, var(--red), var(--red-soft));
  }
  .art-area--back {
    left: 0;
    top: 0;
    width: 230px;
    height: 200px;
  }
  .art-area--front {
    right: 0;
    bottom: 0;
    width: 135px;
    height: 190px;
  }

  .brand-name {
    position: absolute;
    left: 70px;
    top: 36px;
    margin: 0;
    font-size: 44px;
    font-weight: 500;
    color: var(--red);
    letter-spacing: 1px;
  }
  .identity {
    position: absolute;
    left: 40px;
    top: 112px;
    color: var(--ink);
  }
  .identity__name {
    margin: 0;
    font-size: 16px;
    font-weight: 700;
  }
  .identity__role {
    margin: 2px 0 0;
    font-size: 15px;
    font-style: italic;
  }
  .contact {
    position: absolute;
    left: 40px;
    top: 176px;
    margin: 0;
    padding: 0;
    list-style: none;
    color: var(--ink);
    font-size: 16px;
    line-height: 1.3;
  }
  .contact__alt { padding-left: 56px; }
</style>
</head>
<body>
<main class="stage">
  <section class="card card--back" aria-label="Card reverse, space for writing">
    <div class="art-area art-area--back" role="img" aria-label="Red decorative artwork in the top-left corner"></div>
  </section>

  <section class="card card--front" aria-label="Card front">
    <div class="art-area art-area--front" role="img" aria-label="Red decorative artwork in the lower-right corner"></div>
    <p class="brand-name">Remy Vok</p>
    <div class="identity">
      <p class="identity__name">Remy Vok</p>
      <p class="identity__role">Magician | Speaker</p>
    </div>
    <ul class="contact">
      <li>Phone: +32 471 265 903</li>
      <li>Email: book@remy-vok.net</li>
      <li>Website: www.remy-vok.net</li>
      <li class="contact__alt">remy-vok.net</li>
    </ul>
  </section>
</main>
</body>
</html>
```